LEARN Business Skills so you can Earn a good living

size of the poster is 8”x 10.75" plus 0.25" bleed.
Please leave 1 inch on the bottoum for footer
I want a design a poster that will attract people's attention.
I appreciate a creative ad however the ad should not take away from being able to clearly read the text.
-I also appreciate a simple creative ad that is not too busy.
-you can use graphics, vectors, or pictures of real people.
-however, if you use real people it should be a white male that is wearing a white shirt and look like a professional person.

Target Market(s)

Potential young business people

Industry/Entity Type

education

Requirements
Must have
• easy to read the text
Nice to have
• I would like a "creative" simple ad that is easy to be read
Should not have
• pictures of women

```html
<!DOCTYPE html>
<html lang="en">
<head>
<meta charset="utf-8">
<title>Business Enrichment Course</title>
<link href="https://fonts.googleapis.com/css2?family=Bebas+Neue&family=Jost:wght@300;400;600&display=swap" rel="stylesheet">
<style>
  :root {
    --blue: #2f85c8;
    --white: #ffffff;
    --black: #000000;
    --red: #b3120f;
    --green: #66ee10;
    --ink: #111111;
    --icon-blue: #3a8fd0;
  }
  * { margin: 0; padding: 0; box-sizing: border-box; }
  html, body { width: 907px; height: 1200px; overflow: hidden; background: var(--white); }
  .poster { position: relative; width: 907px; height: 1200px; overflow: hidden; background: var(--white); font-family: 'Jost', sans-serif; }
  .top-band { position: absolute; left: 0; top: 0; width: 907px; height: 514px; background: var(--blue); }
  .brand { position: absolute; left: 84px; top: 70px; display: flex; align-items: center; gap: 22px; }
  .brand-mark { width: 72px; height: 72px; border-radius: 50%; background: var(--white); flex: none; }
  .brand-name { color: var(--white); font-family: 'Jost', sans-serif; font-weight: 600; font-size: 46px; line-height: 52px; letter-spacing: 1px; }
  .hero-photo { position: absolute; left: 418px; top: 40px; width: 475px; height: 474px;
    background: linear-gradient(180deg, #3b8ccb 0%, #c9d9ea 55%, #e9eef4 100%);
    border-radius: 200px 200px 0 0; }
  .title-block { position: absolute; background: var(--black); color: var(--white); font-family: 'Bebas Neue', sans-serif; font-size: 98px; line-height: 1; letter-spacing: 11px; padding-left: 20px; display: flex; align-items: center; }
  .title-business { left: 67px; top: 296px; width: 407px; height: 114px; }
  .title-enrichment { left: 67px; top: 410px; width: 519px; height: 104px; }
  .title-course { left: 67px; top: 514px; width: 324px; height: 106px; }
  .tagline { position: absolute; left: 413px; top: 534px; color: var(--red); font-family: 'Bebas Neue', sans-serif; font-size: 38px; line-height: 32px; letter-spacing: 0.4px; }
  .benefits { position: absolute; left: 246px; top: 645px; width: 492px; height: 138px; border: 3px solid var(--ink); border-radius: 40px; background: var(--white); }
  .benefits-heading { position: absolute; left: 19px; top: 7px; font-size: 24.5px; font-weight: 400; color: var(--ink); letter-spacing: 0.4px; white-space: nowrap; }
  .benefit { position: absolute; left: 23px; display: flex; align-items: center; font-size: 22px; color: var(--ink); letter-spacing: 0.6px; white-space: nowrap; }
  .benefit svg { width: 24px; height: 24px; margin-right: 45px; flex: none; }
  .benefit-1 { top: 41px; } .benefit-2 { top: 71px; } .benefit-3 { top: 100px; }
  .presenter { position: absolute; left: 57px; top: 695px; width: 274px; height: 407px;
    background: linear-gradient(180deg, #c6e8d6 0%, #c6e8d6 45%, #1b2a3a 46%, #1b2a3a 100%);
    border-radius: 120px 120px 10px 10px; }
  .bottom-wave { position: absolute; left: 0; top: 0; width: 907px; height: 1200px; }
  .topics { position: absolute; left: 394px; top: 852px; width: 474px; color: var(--white); font-weight: 400; font-size: 19.5px; line-height: 21.5px; text-align: justify; text-align-last: left; letter-spacing: 0.3px; word-spacing: 2px; }
</style>
</head>
<body>
<div class="poster">
  <div class="top-band"></div>
  <div class="hero-photo" role="img" aria-label="Photo of two smiling young businessmen in white shirts and ties, arms crossed"></div>

  <div class="brand">
    <div class="brand-mark"></div>
    <div class="brand-name">BRIGHT<br>PATH<br>ACADEMY</div>
  </div>

  <div class="title-block title-business">BUSINESS</div>
  <div class="title-block title-enrichment">ENRICHMENT</div>
  <div class="title-block title-course">COURSE</div>

  <div class="tagline">A proven success of helping<br>people in their livelihoods</div>

  <svg class="bottom-wave" viewBox="0 0 907 1200" aria-hidden="true">
    <path d="M377 822 Q630 832 882 820 L882 1030 Q790 1060 680 1052 Q560 1042 470 1070 Q420 1090 377 1100 Z" fill="var(--green)"/>
    <path d="M0 1095 Q90 1082 200 1100 Q320 1118 440 1090 Q560 1050 700 1048 Q820 1048 907 1022 L907 1200 L0 1200 Z" fill="var(--blue)"/>
  </svg>

  <div class="presenter" role="img" aria-label="Illustration of a smiling bearded man holding a clipboard and pointing to the skills list"></div>

  <div class="benefits">
    <div class="benefits-heading">BUSINESS SKILLS THAT WILL HELP YOU:</div>
    <div class="benefit benefit-1">
      <svg viewBox="0 0 24 24" aria-hidden="true"><circle cx="12" cy="12" r="12" fill="var(--icon-blue)"/><rect x="6.5" y="8.5" width="11" height="9" rx="1.5" fill="none" stroke="#fff" stroke-width="1.5"/><path d="M10 8.5V7h4v1.5" fill="none" stroke="#fff" stroke-width="1.5"/></svg>
      Get A Quality Job
    </div>
    <div class="benefit benefit-2">
      <svg viewBox="0 0 24 24" aria-hidden="true"><circle cx="12" cy="12" r="12" fill="var(--icon-blue)"/><path d="M7 17v-2M10 17v-4M13 17v-6M16 17v-8" stroke="#fff" stroke-width="1.8"/><path d="M7 12l9-6M13.5 6H16v2.5" fill="none" stroke="#fff" stroke-width="1.3"/></svg>
      Start/Grow Your Business
    </div>
    <div class="benefit benefit-3">
      <svg viewBox="0 0 24 24" aria-hidden="true"><circle cx="12" cy="12" r="12" fill="var(--icon-blue)"/><circle cx="10" cy="9" r="2.5" fill="#fff"/><path d="M5.5 17a4.5 4 0 0 1 9 0Z" fill="#fff"/><path d="M17 7v10M18.5 9h-2.5a1.2 1.2 0 0 0 0 2.4h2a1.2 1.2 0 0 1 0 2.4H15.5" fill="none" stroke="#fff" stroke-width="1.2"/></svg>
      Increase Your Salary
    </div>
  </div>

  <p class="topics">BUSINESS ADMIISTRATION - SMALL BUSINESS MANAGEMENT - FINANCE - INVESTMENTS - COMPUTERS- ACCOUNTING - SALES MARKETING - PROJECT MANAGEMENT INTERVIEWING SKILLS - BUSINESS LAW - NEGOTIATION - PUBLIC SPEAKING - IMPORT/EXPORT - INFORMATION TECHNOLOY - DISTRIBUTION - MARKETING - LEDGERWISE - REAL ESTATE - HEALTH CARE - MANAGEMENT - SHOPSTREAM</p>
</div>
</body>
</html>
```